Plakat für Schaufenster
Zielgruppe
Moin Moin,
ich habe einen kleinen Fahrradladen in einem historischen Gebäude. Wir führen ein sehr hochwertiges und ausgesuchtes Programm diverser Hersteller und bieten eine umfassende individuelle Beratung
Aufgabenstellung
Ein Fahrradladen ist einerseits ein Handwerksbetrieb anderseits auch ein Handelsbetrieb. Da ich als Einzelkämpfer in meinem Laden arbeite, habe ich diese beiden Betriebe zeitlich voneinander getrennt. Ich arbeite Vormittags in der Werkstatt und Nachmitttags ist mein Laden für Service und Beratung geöffnet, d.h. meine Laden ist nur Nachmittags von 14-18 und Samstag von 10-13 Uhr geöffnet. Durch diese Regelung kann ich kurze Reparaturzeiten und gute Beratung bieten.
Leider denken nun viele Menschen wenn Sie Vormittags vor verschlossener Tür stehen: "der hat es nicht nötig und arbeitet nur noch halbe Tage!".
Nun möchte ich mit einem Plakat im Fenster meinen "geteilten" Betrieb bzw. meine Arbeitsteilung erklären.
Vielleicht in Form einer analogen Uhr mit entsprechender Teilung !?! Aber auch andere Ideen sind herzlich Willkommen !!

```html
<!DOCTYPE html>
<html lang="de">
<head>
<meta charset="utf-8">
<title>Werkstattzeit – Service &amp; Beratung</title>
<link rel="stylesheet" href="https://fonts.googleapis.com/css2?family=Vollkorn:wght@700&family=Rosarivo&display=swap">
<style>
  :root {
    --canvas: #ffffff;
    --paper: #f0c992;
    --signal: #ef5534;
    --ink: #121010;
    --cream: #f9dcae;
  }
  * { margin: 0; padding: 0; box-sizing: border-box; }
  html, body { width: 1200px; height: 1200px; overflow: hidden; background: var(--canvas); }
  .poster {
    position: absolute; left: 197px; top: 30px;
    width: 806px; height: 1140px;
    background: linear-gradient(to bottom, var(--paper) 0 570px, var(--signal) 570px 100%);
    font-family: "Rosarivo", Georgia, serif;
    color: var(--ink);
  }
  .frame {
    position: absolute; left: 21px; top: 20px; right: 21px; bottom: 21px;
    border: 1.5px solid var(--ink);
  }
  .line { position: absolute; left: 0; width: 100%; text-align: center; white-space: nowrap; }
  .headline { font-family: "Vollkorn", Georgia, serif; font-weight: 700; font-size: 82px; letter-spacing: -0.5px; line-height: 1; }
  .title { top: 78px; }
  .note { top: 158px; font-size: 31px; line-height: 1; }
  .day { font-size: 32px; line-height: 1; color: var(--signal); }
  .day-1 { top: 262px; }
  .day-2 { top: 311px; }
  .divider { position: absolute; left: 322px; width: 162px; height: 1px; background: var(--ink); }
  .divider-top { top: 238px; }
  .divider-bottom { top: 942px; }
  .bicycle {
    position: absolute; left: 66px; top: 389px; width: 676px; height: 410px;
    background: radial-gradient(ellipse at center, rgba(18,16,16,0.28), rgba(18,16,16,0.08) 70%, rgba(18,16,16,0) 100%);
  }
  .service { top: 842px; }
  .hours { font-size: 32px; line-height: 1; color: var(--cream); }
  .hours-1 { top: 967px; }
  .hours-2 { top: 1017px; }
</style>
</head>
<body>
  <main class="poster">
    <div class="frame"></div>
    <h1 class="line headline title">Werkstattzeit</h1>
    <p class="line note">(kein Service, keine Beratung, kein Verkauf)</p>
    <div class="divider divider-top"></div>
    <p class="line day day-1">Montag - Freitag</p>
    <p class="line day day-2">Vormittag</p>
    <div class="bicycle" role="img" aria-label="Illustration eines historischen Fahrrads in Schwarz"></div>
    <h2 class="line headline service">Service &amp; Beratung</h2>
    <div class="divider divider-bottom"></div>
    <p class="line hours hours-1">Montag - Freitag 14:00 - 18:00 Uhr</p>
    <p class="line hours hours-2">Samstag 10:00 - 13:00 Uhr</p>
  </main>
</body>
</html>
```